Personal Card: Make it roar!

Hello to all designers,
Hope you're having a nice day/evening! Let's cut to the chase. I would like a modern, beautiful and professional personal business card; with a vector-art of a lion. I'd like the lion to be Blood Red. On a black background. I'm a Filipino, and would love to have my country's flag incorporated into the design. Id like the stars of my flag to be used in your designs if possible. The texts I want on the card are only my name, number, and email address. Colour of my name should be White, and my details Silver. The size and font should be simple and professional, you're in charge of that! The placements of the lion and my details will be yours to decide.

At the back of the card, I would like just the words "Thank You" (Silver) on a Black Background. Right on the center.

To summarise, my requirements are:
- Blood Red: Front Face of Lion, Vector-Art
- Black: Background
- Yellow: Three Stars used in the design
- White: Bartholomew Sr Pelaez
- Silver: Number & Email (Where appropriate)
- Back of the card (Center). Silver: "Thank You"
- Please DON'T use the colour blue.

It's all about the Lion. Images you'll find attached are some images of Lions' faces which I particularly want to be captured and put onto the card. Convert it into a vector-art. A vector-art Lion. PLEASE use the images attached for inspiration only! Do not use it on your designs. Thank you very much for your time.

Good luck!

Bart

Hello Desginers, Please use Blood Red for the colour red in your designs:HEX: 8A0707RGB: 138,7,7Thank you,Bart Added Saturday, March 12, 2016

Target Market(s)

Potential Connections

Industry/Entity Type

It Professional

Contact Information for Business Card

Name: Bartholomew Sr Pelaez
Email: bartpelaez@zentomail.example
Number: 07391628047

Requirements
Must have
• Modern, Professional & Simple
• (Blood Red HEX: 8A0707, RGB: 138,7,7) Lion (Vector-style art)
• (Black) Background
• (White) My Name
• (Silver) My Details
• Back of card: "Thank You" in Silver. Font size should be small/medium.
• Only colours that should be used are Red, Black, Yellow and White/Silver
Nice to have
• - Use of 3 Yellow stars on the design
Should not have
• - Please avoid using any other colours apart from those specified.

```html
<!DOCTYPE html>
<html lang="en">
<head>
<meta charset="utf-8">
<title>Bartholomew Sr Pelaez — Business Card</title>
<link href="https://fonts.googleapis.com/css2?family=Open+Sans:wght@400;700&display=swap" rel="stylesheet">
<style>
  :root {
    --backdrop: #2b2624;
    --card-black: #050505;
    --blood-red: #8e1414;
    --divider-red: #2a0808;
    --name-white: #e4e4e4;
    --detail-silver: #c4c4c4;
    --thanks-silver: #b9b9b9;
  }
  * { margin: 0; padding: 0; box-sizing: border-box; }
  html, body {
    width: 1200px;
    height: 844px;
    overflow: hidden;
    background: var(--backdrop);
    font-family: "Open Sans", Arial, sans-serif;
  }
  .stage {
    position: relative;
    width: 1200px;
    height: 844px;
    display: flex;
    align-items: center;
    justify-content: center;
    gap: 60px;
  }
  .card {
    position: relative;
    width: 525px;
    height: 300px;
    background: var(--card-black);
    box-shadow: 0 10px 30px rgba(0,0,0,0.45);
  }
  .card-front .lion-mark {
    position: absolute;
    left: 48px;
    top: 62px;
    width: 185px;
    height: 185px;
    border-radius: 50%;
    background: radial-gradient(circle at 45% 45%, #9a1818 0%, var(--blood-red) 70%, #6e0c0c 100%);
  }
  .card-front .divider {
    position: absolute;
    left: 255px;
    top: 36px;
    width: 1px;
    height: 228px;
    background: linear-gradient(to bottom, transparent, var(--divider-red) 25%, var(--divider-red) 75%, transparent);
  }
  .card-front .details {
    position: absolute;
    left: 278px;
    top: 92px;
  }
  .name {
    font-weight: 700;
    font-size: 20px;
    color: var(--name-white);
    letter-spacing: 0.2px;
    margin-bottom: 12px;
  }
  .contact-line {
    display: flex;
    align-items: center;
    gap: 9px;
    font-size: 15px;
    line-height: 22px;
    color: var(--detail-silver);
  }
  .contact-line svg { width: 11px; height: 11px; flex: none; }
  .card-back {
    display: flex;
    align-items: center;
    justify-content: center;
  }
  .thanks {
    font-size: 19px;
    font-weight: 400;
    color: var(--thanks-silver);
  }
</style>
</head>
<body>
  <main class="stage">
    <section class="card card-front">
      <div class="lion-mark" role="img" aria-label="Blood red vector illustration of a lion's head in profile"></div>
      <div class="divider"></div>
      <div class="details">
        <p class="name">Bartholomew Sr Pelaez</p>
        <p class="contact-line">
          <svg viewBox="0 0 12 12" aria-hidden="true"><path fill="var(--blood-red)" d="M2.4 0.6l2 2.2-1 1.2c0.7 1.5 1.8 2.6 3.4 3.4l1.2-1 2.2 2-1.1 1.9C5 9.7 2.2 7 1 1.7z"/></svg>
          <span>07391628047</span>
        </p>
        <p class="contact-line">
          <svg viewBox="0 0 12 12" aria-hidden="true"><rect x="0.5" y="2" width="11" height="8" fill="var(--blood-red)"/><polyline points="0.8,2.4 6,6.5 11.2,2.4" fill="none" stroke="#050505" stroke-width="1"/></svg>
          <span>bartpelaez@zentomail.example</span>
        </p>
      </div>
    </section>
    <section class="card card-back">
      <p class="thanks">Thank You</p>
    </section>
  </main>
</body>
</html>
```